Bright Oak Fitness Facility Business Cards

Business Card Design that incorporates the logo and tagline

Target Market(s)

Fitness, People Who Exercise

Contact Information for Business Card

2817 Mossgrove Bend Road
Tavares, Florida 32190
Phone: 352-555-Jump (5867)
www.brightoakfitness.example
info@brightoakfitness.example

Requirements
Must have
• Logo, Address, Website, email and tagline "More Than A Gym". Colors should be red/black/grey/white

```html
<!DOCTYPE html>
<html lang="en">
<head>
<meta charset="utf-8">
<title>Bright Oak Fitness Business Cards</title>
<link rel="stylesheet" href="https://fonts.googleapis.com/css2?family=Open+Sans:wght@400;700;800&display=swap">
<style>
  :root {
    --bg: #e9e7e4;
    --card: #ffffff;
    --red: #e31b23;
    --red-dark: #8e0a10;
    --red-deep: #5e0509;
    --black: #111111;
    --white: #ffffff;
    --shadow: rgba(0,0,0,0.18);
  }
  * { margin: 0; padding: 0; box-sizing: border-box; }
  html, body { width: 1200px; height: 1200px; overflow: hidden; }
  body {
    background: var(--bg);
    font-family: "Open Sans", Arial, sans-serif;
    position: relative;
  }
  .card {
    position: absolute;
    left: 150px;
    width: 900px;
    height: 514px;
    background: var(--card);
    box-shadow: 0 8px 24px var(--shadow);
    overflow: hidden;
  }
  .card--back { top: 56px; }
  .card--front { top: 630px; }

  .brand {
    display: flex;
    align-items: center;
    gap: 14px;
    color: var(--red);
    font-weight: 800;
    letter-spacing: 1px;
    white-space: nowrap;
  }
  .brand__dot {
    width: 22px; height: 22px;
    border-radius: 50%;
    background: var(--red);
  }
  .card--back .brand {
    position: absolute;
    top: 50%; left: 50%;
    transform: translate(-50%, -50%);
    font-size: 46px;
  }
  .card--front .brand {
    position: absolute;
    top: 110px; left: 70px;
    font-size: 38px;
  }

  .wave { position: absolute; inset: 0; width: 900px; height: 514px; }

  .tagline {
    position: absolute;
    left: 70px; bottom: 36px;
    color: var(--black);
    font-weight: 800;
    font-size: 34px;
    letter-spacing: 7px;
    text-transform: uppercase;
  }

  .contact {
    position: absolute;
    left: 600px; top: 190px;
    padding-left: 26px;
    border-left: 1px solid rgba(255,255,255,0.25);
    color: var(--white);
    font-size: 16px;
    line-height: 1.55;
    list-style: none;
  }
  .contact__item {
    display: flex;
    align-items: flex-start;
    gap: 12px;
    margin-bottom: 8px;
  }
  .contact__icon { width: 16px; height: 16px; flex: none; margin-top: 4px; }
</style>
</head>
<body>

  <section class="card card--back" aria-label="Business card back">
    <div class="brand"><span class="brand__dot"></span>BRIGHT OAK FITNESS</div>
  </section>

  <section class="card card--front" aria-label="Business card front">
    <svg class="wave" viewBox="0 0 900 514" aria-hidden="true">
      <defs>
        <linearGradient id="redFill" x1="0" y1="0" x2="1" y2="1">
          <stop offset="0" stop-color="#c3121a"/>
          <stop offset="0.45" stop-color="#a80d14"/>
          <stop offset="1" stop-color="#7e080d"/>
        </linearGradient>
        <radialGradient id="sheen" cx="0.45" cy="0.45" r="0.35">
          <stop offset="0" stop-color="#ff2a33" stop-opacity="0.7"/>
          <stop offset="1" stop-color="#ff2a33" stop-opacity="0"/>
        </radialGradient>
      </defs>
      <path d="M0,345 C160,430 330,410 420,270 C510,130 640,85 900,78 L900,514 L0,514 Z" fill="var(--red-deep)"/>
      <path d="M0,362 C170,440 345,420 432,285 C520,150 650,100 900,96 L900,514 L0,514 Z" fill="url(#redFill)"/>
      <path d="M0,362 C170,440 345,420 432,285 C520,150 650,100 900,96 L900,514 L0,514 Z" fill="url(#sheen)"/>
      <path d="M0,362 C170,440 345,420 432,285 C520,150 650,100 900,96" fill="none" stroke="#ff3b42" stroke-width="2"/>
    </svg>

    <div class="brand"><span class="brand__dot"></span>BRIGHT OAK FITNESS</div>

    <ul class="contact">
      <li class="contact__item">
        <svg class="contact__icon" viewBox="0 0 16 16" aria-hidden="true"><path d="M8 1a5 5 0 0 0-5 5c0 4 5 9 5 9s5-5 5-9a5 5 0 0 0-5-5zm0 7a2 2 0 1 1 0-4 2 2 0 0 1 0 4z" fill="#fff"/></svg>
        <span>2817 Mossgrove Bend Road<br>Tavares, Florida 32190</span>
      </li>
      <li class="contact__item">
        <svg class="contact__icon" viewBox="0 0 16 16" aria-hidden="true"><path d="M4 2l2.5 3-1.5 1.5c1 2 2.5 3.5 4.5 4.5L11 9.5 14 12l-1.5 2C7 14 2 9 2 3.5z" fill="#fff"/></svg>
        <span>352-555-Jump (5867)</span>
      </li>
      <li class="contact__item">
        <svg class="contact__icon" viewBox="0 0 16 16" aria-hidden="true"><circle cx="8" cy="8" r="6.5" fill="none" stroke="#fff" stroke-width="1.4"/><path d="M1.5 8h13M8 1.5c-3 3.5-3 9.5 0 13M8 1.5c3 3.5 3 9.5 0 13" fill="none" stroke="#fff" stroke-width="1.2"/></svg>
        <span>www.brightoakfitness.example</span>
      </li>
      <li class="contact__item">
        <svg class="contact__icon" viewBox="0 0 16 16" aria-hidden="true"><rect x="1.5" y="3.5" width="13" height="9" fill="none" stroke="#fff" stroke-width="1.4"/><path d="M1.5 3.5L8 9l6.5-5.5" fill="none" stroke="#fff" stroke-width="1.4"/></svg>
        <span>info@brightoakfitness.example</span>
      </li>
    </ul>

    <p class="tagline">More Than A Gym</p>
  </section>

</body>
</html>
```